Webshop Template

For our Webstore in UK we need a complete Template,
shoppingcart is Magento, the Shop is focussed on Download software,

the name: Appvaultdepot.co.uk

Check out some other good stores, like lumawerk.de

for example the Page from 

www.brenvik.co.uk or

www.lumawerk.de

www.tastenhugo.de

www.klickrabatt.de

The Logodesign which are in Consideration

http://www.artmosaiq.com/design/5520817/logo-design-by-tomasz7kv

http://www.artmosaiq.com/design/5518360/logo-design-by-luisgaviota

http://www.artmosaiq.com/design/5517245/logo-design-by-kestrel-works

http://www.artmosaiq.com/design/5516093/logo-design-by-zumbiloft

http://www.artmosaiq.com/design/5515471/logo-design-by-tivaro

http://www.artmosaiq.com/design/5514902/logo-design-by-blue-fern-graphics-

Target Market(s)

B2C - Consumer Marcet

Industry/Entity Type

Shop

```html
<!DOCTYPE html>
<html lang="en">
<head>
<meta charset="utf-8">
<title>Appvaultdepot – Download Software Store</title>
<link rel="stylesheet" href="https://fonts.googleapis.com/css2?family=Arimo:wght@400;700&family=Open+Sans:wght@700&family=Oswald:wght@500&display=swap">
<style>
:root{
  --green:#6aa82d;
  --green-dark:#4f8a1c;
  --green-light:#8cc63f;
  --orange:#ff6a00;
  --ink:#333;
  --muted:#555;
  --line:#d9d9d9;
  --bar:#444;
}
*{box-sizing:border-box;margin:0;padding:0}
html,body{width:1029px;height:1200px;overflow:hidden;background:#fff}
body{font-family:Arimo,Arial,sans-serif;color:var(--ink)}
.page{position:relative;width:1190px;height:1400px;transform:scale(.857);transform-origin:0 0}
.abs{position:absolute}

/* header */
.header{left:134px;top:13px;width:932px;height:117px;border:1px solid var(--line);background:linear-gradient(#fff,#e9e9e9)}
.brand{left:24px;top:30px;display:flex;align-items:center;gap:12px}
.brand-dot{width:46px;height:46px;border-radius:50%;background:#3a9bd5}
.brand-name{font-size:32px;font-weight:400;color:#444;letter-spacing:-1px}
.toplinks{right:12px;top:25px;font-size:12.5px;font-weight:700;color:#555;word-spacing:2px}
.search-input{left:618px;top:63px;width:238px;height:28px;border:1px solid #ccc;background:#fff}
.search-btn{left:859px;top:63px;width:58px;height:28px;background:#666;color:#fff;font-size:11px;font-weight:700;display:flex;align-items:center;justify-content:center}

/* nav */
.nav{left:134px;top:134px;width:932px;height:47px;background:linear-gradient(#8cc63f,#5e9e24);border:1px solid var(--green-dark);display:flex;align-items:center;padding-left:14px}
.nav a{color:#fff;font-weight:700;font-size:13.5px;text-decoration:none;padding:0 25px;border-right:1px solid rgba(255,255,255,.3);line-height:30px}
.nav a:last-child{border:none}

/* sidebar */
.sidebar{left:134px;top:186px;width:222px;height:811px;border:1px solid #e5e5e5}
.cat{position:absolute;left:8px;width:207px;height:35px;background:linear-gradient(#f4f8fa,#dbe6ec);border:1px solid #d3dde3;font-size:13.5px;padding:10px 8px;color:#222}
.sub{position:absolute;left:8px;width:207px;height:30px;border-bottom:1px solid #d6d6d6;font-size:12.5px;padding:8px 16px;color:#222}
.sub::before{content:"";display:inline-block;border-left:4px solid #333;border-top:3.5px solid transparent;border-bottom:3.5px solid transparent;margin-right:6px}
.sellers{position:absolute;left:8px;top:498px;width:204px;height:300px;border:1px solid #b9d0da;background:linear-gradient(#fff,#dce9ef)}
.sellers h3{font-family:"Open Sans",sans-serif;color:var(--green);font-size:16px;margin:10px 0 10px 10px}
.sellers li{list-style:none;font-size:13.5px;margin:0 0 6px 6px;height:18px;display:flex;align-items:center;gap:8px}
.sellers li::before{content:"›";width:10px;height:10px;border:1px solid #999;font-size:10px;line-height:8px;text-align:center;color:#555}
.more{position:absolute;left:1px;bottom:2px;width:200px;height:26px;background:linear-gradient(var(--green-light),var(--green-dark));color:#fff;font-size:12.5px;font-weight:700;text-align:right;padding:6px 14px}

/* banner */
.banner{left:362px;top:186px;width:703px;height:250px;background:linear-gradient(90deg,#c9d7df,#dfe8ed 60%,#cfdce4);border:1px solid #c3cfd6;overflow:hidden}
.boxes{position:absolute;left:75px;top:8px;width:310px;height:232px;background:linear-gradient(90deg,#7fc21c 0,#5ea812 40%,#1d3357 45%,#0e1d36);border-radius:2px}
.price{position:absolute;left:0;top:157px;width:366px;height:52px;background:linear-gradient(var(--orange),#e85500);display:flex;align-items:center;color:#fff}
.price small{width:160px;text-align:right;font-size:13.5px;line-height:18px;padding-right:12px}
.price b{font-family:Oswald,sans-serif;font-size:48px;font-weight:500}
.price sup{font-family:Oswald,sans-serif;font-size:17px;align-self:flex-start;margin-top:4px}
.cart-tab{position:absolute;left:312px;top:157px;width:54px;height:52px;background:var(--green)}
.banner h2{position:absolute;left:402px;top:56px;font-family:"Open Sans",sans-serif;font-size:29px;color:var(--green);letter-spacing:1px}
.banner p{position:absolute;left:404px;top:98px;width:260px;font-size:14.5px;line-height:20px;color:#222}

.ship{left:362px;top:441px;width:703px;height:77px;background:linear-gradient(#8cc63f,#5e9e24);border:1px solid var(--green-dark);color:#fff}
.parcel{position:absolute;left:232px;top:6px;width:64px;height:66px;background:linear-gradient(#d7b27a,#a8804a);border-radius:4px}
.ship h3{position:absolute;left:302px;top:14px;font-size:21px;font-weight:400}
.ship h3 b{font-size:27px}
.ship p{position:absolute;left:303px;top:45px;font-size:15px;color:#eaf5d9}
.ship a{position:absolute;left:594px;top:45px;background:#2a3d5c;padding:3px 9px;font-size:12.5px;font-weight:700;color:#fff}

.newbar{left:362px;top:521px;width:704px;height:44px;background:linear-gradient(#666,#3a3a3a);color:#fff;font-size:12.5px;font-weight:700;padding:15px 40px}
.newbar::before{content:"♡";position:absolute;left:16px;top:12px;font-size:15px;color:#ddd}

/* products */
.card{position:absolute;width:232px;height:211px;border:1px solid #dde5ea}
.card h4{text-align:center;font-size:14px;margin-top:12px;letter-spacing:.3px}
.pack{width:84px;height:118px;margin:14px auto 0;border-radius:3px}
.actions{position:absolute;left:0;bottom:0;width:100%;height:30px;background:#dfe8ee;display:flex;align-items:center;padding-left:18px;gap:14px}
.btn{height:20px;font-size:12px;font-weight:700;color:#fff;display:flex;align-items:center;padding:0 10px}
.btn-details{background:var(--green)}
.btn-cart{background:#444;padding-right:0}
.btn-cart i{width:20px;height:20px;background:var(--green);margin-left:2px}

/* brands */
.brands{left:134px;top:1004px;width:932px;height:82px;border-top:3px solid #b9c7cf;background:linear-gradient(#f4f4f4,#fff);display:flex;justify-content:space-around;align-items:center;color:#9a9a9a;font-size:20px;font-weight:700;letter-spacing:1px}

/* footer */
.footer{left:132px;top:1097px;width:934px;height:234px;border:1px solid var(--line);background:#f8f8f8}
.col{position:absolute;top:18px}
.col h5{font-size:13.5px;font-weight:700;color:#333;margin-bottom:14px}
.col li{list-style:none;font-size:12px;color:var(--muted);line-height:22px}
.col .phone{color:var(--orange);font-size:14.5px;margin-top:12px}
.pay{display:grid;grid-template-columns:repeat(3,46px);gap:6px}
.pay span{height:30px;border:1px solid #ccc;background:#fff;font-size:9px;font-weight:700;color:#555;display:flex;align-items:center;justify-content:center}
.copy{left:138px;top:1350px;font-size:12px;color:#333}
.follow{right:126px;top:1350px;display:flex;align-items:center;gap:8px;font-size:12.5px;font-weight:700;color:#333}
.follow span{font-size:10px;font-weight:400;color:#555}
</style>
</head>
<body>
<div class="page">

  <header class="header abs">
    <div class="brand abs"><span class="brand-dot"></span><span class="brand-name">appvaultdepot</span></div>
    <div class="toplinks abs">My Account &nbsp;|&nbsp; My Cart &nbsp;|&nbsp; Checkout &nbsp;|&nbsp; My Wishlist &nbsp;|&nbsp; Log In</div>
    <div class="search-input abs"></div>
    <div class="search-btn abs">Search</div>
  </header>

  <nav class="nav abs">
    <a>Home</a><a>Download</a><a>Products</a><a>Reviews</a><a>Forum</a><a>About</a><a>Contacts</a>
  </nav>

  <aside class="sidebar abs">
    <div class="cat" style="top:9px">Security Software</div>
    <div class="sub" style="top:46px">Mac Software</div>
    <div class="sub" style="top:77px">Performance</div>
    <div class="sub" style="top:107px">Finance</div>
    <div class="sub" style="top:138px">Design</div>
    <div class="sub" style="top:168px">Multimedia</div>
    <div class="cat" style="top:201px">Digital Photo Software</div>
    <div class="cat" style="top:241px">Mac Software</div>
    <div class="cat" style="top:281px">Performance</div>
    <div class="cat" style="top:321px">Finance</div>
    <div class="cat" style="top:361px">Design</div>
    <div class="cat" style="top:401px">Multimedia</div>
    <div class="cat" style="top:441px">Home &amp; Family</div>
    <div class="sellers">
      <h3>Top Sellers</h3>
      <ul>
        <li>Glasswing 7</li><li>Home</li><li>Premium 64</li><li>Hologramm</li><li>DVD und</li>
        <li>Glasswing 7</li><li>Hologramm</li><li>DVD und</li><li>Glasswing 7</li>
      </ul>
      <div class="more">read more ›</div>
    </div>
  </aside>

  <section class="banner abs">
    <div class="boxes" role="img" aria-label="Two software boxes, green and dark blue"></div>
    <div class="price"><small>Price After<br>Rebate</small><b>$799</b><sup>.99</sup></div>
    <div class="cart-tab"><svg width="54" height="52" viewBox="0 0 54 52"><path d="M14 17h5l4 13h14l3-10H21" fill="none" stroke="#fff" stroke-width="2.5"/><circle cx="25" cy="35" r="2.5" fill="#fff"/><circle cx="35" cy="35" r="2.5" fill="#fff"/></svg></div>
    <h2>Effective Software</h2>
    <p>Simply dummy text of the printing and typesetting industry. Lorem Ipsum has been the industry's standard dummy text ever since the 1500s.</p>
  </section>

  <section class="ship abs">
    <div class="parcel" role="img" aria-label="Cardboard shipping parcel"></div>
    <h3>Free shipping on order over <b>$50</b></h3>
    <p>This offer is valid on all our store items.</p>
    <a>read more</a>
  </section>

  <div class="newbar abs">NEW PRODUCTS</div>

  <section class="products">
    <div class="card" style="left:362px;top:569px"><h4>Standard Soft Package</h4><div class="pack" role="img" aria-label="Dark software box" style="background:linear-gradient(135deg,#222,#6b7f9a)"></div><div class="actions"><span class="btn btn-details">Details</span><span class="btn btn-cart">Add to Cart<i></i></span></div></div>
    <div class="card" style="left:598px;top:569px"><h4>Standard Soft Package</h4><div class="pack" role="img" aria-label="Orange software box" style="background:linear-gradient(135deg,#ffd23c,#f07d00)"></div><div class="actions"><span class="btn btn-details">Details</span><span class="btn btn-cart">Add to Cart<i></i></span></div></div>
    <div class="card" style="left:835px;top:570px"><h4>Standard Soft Package</h4><div class="pack" role="img" aria-label="Yellow software box" style="background:linear-gradient(135deg,#fff3b0,#f4a21c)"></div><div class="actions"><span class="btn btn-details">Details</span><span class="btn btn-cart">Add to Cart<i></i></span></div></div>
    <div class="card" style="left:362px;top:784px"><h4>Standard Soft Package</h4><div class="pack" role="img" aria-label="Light blue software box" style="background:linear-gradient(135deg,#e8eef6,#5a7fb8)"></div><div class="actions"><span class="btn btn-details">Details</span><span class="btn btn-cart">Add to Cart<i></i></span></div></div>
    <div class="card" style="left:598px;top:784px"><h4>Standard Soft Package</h4><div class="pack" role="img" aria-label="Red software box" style="background:linear-gradient(135deg,#e0252b,#8d0c10)"></div><div class="actions"><span class="btn btn-details">Details</span><span class="btn btn-cart">Add to Cart<i></i></span></div></div>
    <div class="card" style="left:835px;top:785px"><h4>Standard Soft Package</h4><div class="pack" role="img" aria-label="Blue software box" style="background:linear-gradient(135deg,#9cc4ea,#1a4c96)"></div><div class="actions"><span class="btn btn-details">Details</span><span class="btn btn-cart">Add to Cart<i></i></span></div></div>
  </section>

  <section class="brands abs">
    <span>Orchard</span><span>Kestra</span><span>Valdo</span><span>Brenvik</span><span>Nuvio</span><span>Tamari</span><span>Sorenta</span><span>Lumo</span>
  </section>

  <footer class="footer abs">
    <div class="col" style="left:40px"><h5>Information</h5><ul><li>About Us</li><li>Customer Service</li><li>Privacy Policy</li><li>Site Map</li><li>Search Terms</li><li>Advanced Search</li><li>Orders and Returns</li><li>Contact Us</li></ul></div>
    <div class="col" style="left:200px"><h5>Why buy from us</h5><ul><li>Shipping &amp; Returns</li><li>Secure Shopping</li><li>International Shipping</li><li>Affiliates</li><li>Group Sales</li></ul></div>
    <div class="col" style="left:360px"><h5>My account</h5><ul><li>Sign In</li><li>View Cart</li><li>My Wishlist</li><li>Track My Order</li><li>Help</li></ul></div>
    <div class="col" style="left:520px"><h5>Store Location</h5><ul><li>42 Kelvin Lane,</li><li>Glasgow, G12 8QP</li></ul><h5 style="margin-top:14px">Order online</h5><div class="phone">1 800 555-0142</div></div>
    <div class="col" style="left:706px"><h5>Easy payment</h5><div class="pay"><span>Paywell</span><span>Cardix</span><span>Sendly</span><span>Amberline</span><span>Billmore</span><span>Parcelo</span></div></div>
  </footer>

  <div class="copy abs">Copyright © 2012 appvaultdepot. All Rights Reserved.</div>
  <div class="follow abs">Follow us <span>Folkboard</span><span>Chirply</span><span>Circlespot</span><span>Vidstream</span></div>

</div>
</body>
</html>
```